Freelance yoga teacher looking for professional postcard design

I need a postcard that shows my class times & venues. I also would like it to show that I offer private one to one sessions for those not ready for group practice, or who require personal attention. It needs to show my contact details - mob: 07344120588, email & website addresses. I also want the opportunity to add other services in future, such as my website and yoga massage.

UPDATE 18 JULY

FRONT OF POSTCARD
I would like the front side of the postcard to not look too busy or 'wordy'. If using bullet points, be creative, so no ticks. Please use my full name Maren T Holloway NCM Dip.

REVERSE SIDE
The reverse side I think should have the NCM logo, together with words describing classes, 'classes are designed...' please omit the sentences starting 'by running courses...'

'Postage required' or lines for an address are not required.

Make the 'where I teach' venues/times look personable, so no harsh gridlines please.

Target Market(s)

Most of my students are 30+ professionals with disposable income or early retirees.

Industry/Entity Type

Teacher

Requirements
Must have
• It must show my National Circle of Movement Teacher Logo which I can supply.
Maren T Holloway is a National Circle of Movement trained teacher.
Classes are small and friendly, designed to create ease in the body, reduce stress and promote relaxation. Julie is passionate about sharing yoga, respecting each individual and modifying to suit their needs, leading to improved function, mobility and stability.

Keep any images simple, such as rolled up yoga mats. I am commissioning a personal mandala which I will use as a logo, but this will not be ready until mid to late August.

Please see attached 'attempt' at a postcard giving details of classes/venues, contact info.
Nice to have
• Somewhere on the postcard the words: 'Yoga. Centre the body & mind. Stretch the possibilities.'
Should not have
• Images of people doing yoga or silhouettes of yoga postures.

```html
<!DOCTYPE html>
<html lang="en">
<head>
<meta charset="utf-8">
<title>Yoga with Maren Holloway – Postcard</title>
<link rel="stylesheet" href="https://fonts.googleapis.com/css2?family=Alike&family=Roboto+Condensed:wght@400;700&display=swap">
<style>
  :root {
    --page: #ffffff;
    --front-teal: #00b193;
    --back-teal: #7ecfcf;
    --pattern-light: #7fd3cf;
    --pattern-deep: #07a99c;
    --ink-green: #0c3d2e;
    --label-green: #0b5b3c;
    --bar-pale: #6fcfc9;
    --bar-deep: #00806b;
    --bar-stone: #7b7a66;
    --panel: rgba(170, 182, 182, 0.92);
    --white: #ffffff;
    --shadow: rgba(0, 0, 0, 0.55);
  }
  * { box-sizing: border-box; margin: 0; padding: 0; }
  html, body { width: 1200px; height: 1000px; overflow: hidden; background: var(--page); }
  .canvas { position: relative; width: 1200px; height: 1000px; }

  .postcard {
    position: absolute; top: 340px; width: 441px; height: 337px;
    overflow: hidden; box-shadow: 6px 7px 6px var(--shadow);
  }
  .postcard--front { left: 108px; background: var(--front-teal); }
  .postcard--back { left: 657px; width: 440px; background: var(--back-teal); }

  .serif { font-family: "Alike", Georgia, serif; }

  /* Front */
  .front-pattern { position: absolute; left: 0; top: 0; }
  .front-title { position: absolute; left: 199px; top: 46px; font-size: 84px; line-height: 1; color: var(--ink-green); letter-spacing: -1px; }
  .front-with { position: absolute; left: 347px; top: 132px; font-size: 17px; color: var(--white); }
  .front-name { position: absolute; left: 204px; top: 151px; font-size: 27px; color: var(--white); white-space: nowrap; }
  .front-qual { position: absolute; left: 354px; top: 183px; font-size: 10px; color: var(--white); }

  .service { position: absolute; left: 0; width: 441px; height: 16px; }
  .service__label {
    position: absolute; top: 0; height: 16px; padding: 0 5px;
    background: var(--label-green); color: var(--white);
    font-size: 11px; line-height: 16px; white-space: nowrap;
  }
  .service__bar { position: absolute; top: 0; right: 0; height: 16px; }

  /* Back */
  .back-pattern { position: absolute; right: 0; top: 0; }
  .teacher-mark {
    position: absolute; left: 18px; top: 23px; width: 68px; height: 68px;
    border-radius: 50%; background: var(--white);
    display: flex; align-items: center; justify-content: center; text-align: center;
    font-size: 8px; line-height: 1.25; color: var(--ink-green);
  }
  .back-title { position: absolute; left: 108px; top: 70px; font-size: 54px; line-height: 1; color: var(--ink-green); }
  .back-tagline { position: absolute; right: 222px; top: 130px; text-align: right; font-size: 8.5px; line-height: 11px; color: var(--ink-green); }
  .back-about { position: absolute; left: 32px; top: 163px; width: 205px; font-size: 8.6px; line-height: 10.5px; color: var(--ink-green); }
  .back-about p + p { margin-top: 10px; }
  .back-contact { position: absolute; left: 32px; top: 271px; font-size: 10.5px; line-height: 14px; color: var(--ink-green); }

  .schedule {
    position: absolute; left: 236px; top: 36px; width: 168px; height: 280px;
    border-radius: 14px; background: var(--panel);
    font-family: "Roboto Condensed", Arial, sans-serif; font-size: 7px; line-height: 8.4px; color: #1a1a1a;
    padding: 25px 10px 0 12px;
  }
  .schedule__row { display: grid; grid-template-columns: 82px 1fr; }
  .schedule__head { font-weight: 700; padding-bottom: 10px; border-bottom: 1px dotted var(--white); margin-bottom: 6px; }
  .schedule__entry { padding-bottom: 5px; border-bottom: 1px dotted var(--white); margin-bottom: 6px; }
  .schedule__entry:last-child { border-bottom: 0; }
</style>
</head>
<body>
<div class="canvas">

  <section class="postcard postcard--front serif">
    <svg class="front-pattern" width="175" height="337" viewBox="0 0 175 337" role="img" aria-label="Flowing leaf-swirl ornament forming a half mandala">
      <path d="M0 0 H40 C120 15 170 80 168 170 C166 260 110 320 40 337 H0 Z" fill="var(--pattern-light)" opacity="0.55"/>
    </svg>
    <div class="front-title">Yoga</div>
    <div class="front-with">with</div>
    <div class="front-name">Maren Holloway</div>
    <div class="front-qual">NCM Dip.</div>

    <div class="service" style="top:225px">
      <span class="service__label" style="left:131px">Group classes</span>
      <span class="service__bar" style="left:213px;background:var(--bar-pale)"></span>
    </div>
    <div class="service" style="top:244px">
      <span class="service__label" style="left:166px">Private Instruction</span>
      <span class="service__bar" style="left:266px;background:var(--bar-deep)"></span>
    </div>
    <div class="service" style="top:264px">
      <span class="service__label" style="left:140px">Therapeutic Thai Yoga Massage</span>
      <span class="service__bar" style="left:310px;background:var(--bar-stone)"></span>
    </div>
  </section>

  <section class="postcard postcard--back serif">
    <svg class="back-pattern" width="90" height="337" viewBox="0 0 90 337" role="img" aria-label="Flowing leaf-swirl ornament along the right edge">
      <path d="M90 0 V337 H30 C60 290 20 240 50 190 C75 140 20 90 55 40 C65 20 70 8 72 0 Z" fill="var(--pattern-deep)" opacity="0.85"/>
    </svg>

    <div class="teacher-mark">NCM<br>Teacher</div>

    <div class="back-title">Yoga</div>
    <div class="back-tagline">Centre the body &amp; mind.<br>Stretch the possibilities.</div>

    <div class="back-about">
      <p>Yoga with Maren Holloway<br>Classes are small and friendly, designed to create ease in the body, reduce stress and promote relaxation.</p>
      <p>Maren is passionate about sharing yoga, respecting each individual and modifying to suit their needs, leading to improved function, mobility and stability.</p>
    </div>

    <div class="back-contact">
      Mob: 07344120588<br>
      Email: marenhollowayyoga@postmail.co.uk<br>
      www.marensyoga.uk
    </div>

    <div class="schedule">
      <div class="schedule__row schedule__head"><span>Venue</span><span>Days/Times</span></div>
      <div class="schedule__row schedule__entry">
        <span>The Orchard Health &amp;<br>Beauty Therapy Centre,<br>Elmbridge</span>
        <span>Monday<br>1.45pm - 3.00pm<br>Tuesday<br>5pm – 6.15pm<br>Thursday<br>6.15pm–7.30pm</span>
      </div>
      <div class="schedule__row schedule__entry">
        <span>Linden Trust,<br>Ashcombe Court Studio,<br>Ashcombe, Elmbridge</span>
        <span>Monday<br>6.30pm - 8.00pm<br>Tuesday<br>10.15am -11.30am</span>
      </div>
      <div class="schedule__row schedule__entry" style="padding-bottom:18px">
        <span>TCVS, Thornwick</span>
        <span>Wednesday<br>5.30pm–7pm &amp;<br>7.30pm–8.45pm</span>
      </div>
      <div class="schedule__row schedule__entry">
        <span>Meridian<br>Well Being Centre,<br>Thornwick</span>
        <span>Wednesday<br>12.15pm-1.30pm</span>
      </div>
    </div>
  </section>

</div>
</body>
</html>
```